Tallow Brook Website - Sell Outdoor product

We are a mom and pop company that just opened our website.

We need a fresh, professional, and nice looking website for our outdoor products. We sell hunting, camping, fishing, and hiking products/accessories to name a few. Some of these products are optics, gun safes, gun bi-pods and tripods, gun lights, hunting camera, tents, hearing protection, targets, fishing poles, and hiking backpacks to name a few.

Our current website is: http://www.tallowbrook.example . You'll see our logo on the website, and it is attached. We aren't married to this logo, so if the designer thinks they can modify it or even come up with a better design for the website, they are more than welcome to do so. We need someone with good images of their own (clip art and/or outdoor images) they can use if they need to for our website.

I also attached a idea I had in visio, but please don't think this is set in stone. It is just a very rough idea. You can also go to our zintaro site to see what we sell: www.zintaro.example/shops/q7xk402mdrvp3s . Right now we sell everything on Zintaro, but our website will just focus on outdoor product. So please make it an outdoor focused website. And you can be creative with some of the product category names. We also want to leave room for some parallel product in the future. Like garden tools, back yard furniture, and BBQs.

Our company also wants to include a deals section on the website. We will probably update it once a week or month. I have included what I did for a deal and accompanying images for it. Image is called Morvelki (And the main images are 01 and 02).

We also want to make sure the file is compatible with our current web-hosting company, https://www.shelvora.example. So I included a webpage layout zip folder. If you have any questions, please contact me.

This is for a PSD and HTML/CSS webpage. If you have any artwork or images that you own and want to use them for the webpage, please do so.

Target Market(s)

The hunter, outdoors person, camper, hiker, and etc.

Industry/Entity Type

It Company

Coding

Coded - Design and coding required

Number of Pages Required

3 page

Requirements
Must have
• The main page. PSD and HTML/CSS file.
• The category page. PSD and HTML/CSS file
• The product display page. PSD and HTML/CSS file
• Please also use some images that you have or from the sites below:
• You can get free stock images for 7 days (20 per day) from this site:
• https://www.pixelbarn.example/complimentary/KTRPLQX/?utm_source=KTRPLQFreeX&utm_medium=cpc&utm_campaign=KTRPLQFreeX&gclid=ZXPq8rTmwnB4DHuLoPeaWs2kTb
• Has 14 good sites:
• http://www.ventureledger.example/article/519372
• Here are the ones I like:
• https://clearpane.example/
• http://grandolim.example/
• http://www.sitewright.example/free/nature
• http://www.dustvault.example/archive
• http://tinyframes.example/
• http://olq.brvkmt.example/search/hiking
• http://fetchqovi.blogspin.example/
• http://roelvastor.example/post/584930271164/download
• http://openvaultlibrary.example/
• If there is a photographer listed on or next to the image, on the bottom lower corner of the image, please put the photographer's name.
Nice to have
• I would like to have an unsubscribe page. If the designer has any of their own images of the outdoor world, and they want to use them, please do. Just make the right graphic changes to make it look good.
Should not have
• Try and keep green color to a minimum.

```html
<!DOCTYPE html>
<html lang="en">
<head>
<meta charset="utf-8">
<title>Tallow Brook — Outdoor Equipment</title>
<link href="https://fonts.googleapis.com/css2?family=Rokkitt:wght@400;500;600&family=Josefin+Slab:wght@400;600;700&display=swap" rel="stylesheet">
<style>
:root{
  --yellow:#f5c118;
  --yellow-deep:#e8b10c;
  --ink:#1c1c1c;
  --grey:#777;
  --grey-light:#bbb;
  --line:#e4e4e4;
  --white:#fff;
}
*{margin:0;padding:0;box-sizing:border-box}
html,body{width:672px;height:1200px;overflow:hidden;background:var(--white)}
body{position:relative;font-family:"Josefin Slab",serif;color:var(--ink)}
a{color:inherit;text-decoration:none}
ul{list-style:none}

/* top bar */
.utility{position:absolute;top:0;left:0;width:672px;height:24px;border-bottom:1px solid var(--line);
  display:flex;justify-content:flex-end;align-items:center;gap:14px;padding-right:103px;white-space:nowrap;
  font-size:6.5px;letter-spacing:.6px;text-transform:uppercase;color:#555;font-weight:600}
.utility .accent{color:var(--yellow)}
.utility .cart{display:flex;align-items:center;gap:5px}
.utility .dots{display:flex;gap:4px}
.utility .dots i{width:6px;height:6px;border-radius:50%;background:var(--yellow);display:block}

/* brand */
.brand{position:absolute;top:50px;left:0;width:672px;text-align:center}
.brand-name{display:inline-flex;align-items:center;gap:7px;font-family:"Rokkitt",serif;font-weight:600;
  font-size:24px;letter-spacing:1px;text-transform:uppercase;color:var(--yellow);white-space:nowrap}
.brand-name i{width:11px;height:11px;background:var(--yellow);display:block}
.currency{position:absolute;top:41px;right:103px;font-size:8px;font-weight:600;letter-spacing:.5px;text-transform:uppercase;color:#555;white-space:nowrap}
.currency span{color:var(--yellow)}

/* nav */
.main-nav{position:absolute;top:102px;left:96px;width:478px;display:flex;justify-content:space-between;align-items:center;
  font-size:6px;font-weight:600;letter-spacing:.3px;text-transform:uppercase;color:#444;white-space:nowrap}
.main-nav a{padding:5px 5px}
.main-nav a.active{border:1px solid var(--yellow)}

/* hero */
.hero{position:absolute;top:130px;left:0;width:672px;height:287px;
  background:linear-gradient(180deg,#9aa3a6 0%,#b7bcbc 30%,#7d8582 60%,#4d4f4a 100%)}
.hero-title{position:absolute;top:100px;width:100%;text-align:center;font-family:"Rokkitt",serif;font-weight:500;color:var(--white);
  font-size:15px;letter-spacing:1.5px;text-transform:uppercase;white-space:nowrap}
.search{position:absolute;top:156px;left:180px;width:340px;height:31px;display:flex}
.search-field{flex:1;background:var(--yellow);color:#fff;font-size:9px;font-weight:600;text-transform:uppercase;
  letter-spacing:.6px;padding-left:10px;display:flex;align-items:center}
.search-btn{width:47px;background:var(--yellow-deep);display:flex;align-items:center;justify-content:center}
.slide-arrow{position:absolute;top:136px;width:28px;height:26px;border:1px solid rgba(255,255,255,.7);display:flex;align-items:center;justify-content:center}
.slide-arrow.prev{left:-1px}.slide-arrow.next{right:-1px}
.photo-credit{position:absolute;left:9px;bottom:6px;font-size:7px;color:#eee;text-transform:uppercase;letter-spacing:.4px;font-weight:600}

/* about */
.about{position:absolute;top:417px;left:0;width:672px;text-align:center}
.about h2{margin-top:21px;font-family:"Rokkitt",serif;font-weight:500;font-size:16px;letter-spacing:1px;text-transform:uppercase}
.about .lead{margin-top:3px;font-size:7.5px;color:var(--yellow);text-transform:uppercase;letter-spacing:.5px;font-weight:600;white-space:nowrap}
.about p.body{width:300px;margin:4px auto 0;font-size:7px;line-height:8.5px;color:var(--grey);text-transform:uppercase;letter-spacing:.3px}
.read-more{position:absolute;top:515px;left:300px;width:66px;height:13px;background:var(--white);z-index:2;
  font-size:7px;font-weight:700;text-transform:uppercase;letter-spacing:.5px;display:flex;align-items:center;justify-content:center;white-space:nowrap}

/* products */
.products{position:absolute;top:517px;left:0;width:672px;height:445px;
  background:radial-gradient(ellipse at 50% 35%,#2c3034 0%,#15181a 55%,#070808 100%)}
.products h2{position:absolute;top:41px;width:100%;text-align:center;font-family:"Rokkitt",serif;font-weight:500;
  color:var(--yellow);font-size:19px;letter-spacing:1.2px;text-transform:uppercase}
.product-grid{position:absolute;top:88px;left:97px;display:grid;grid-template-columns:repeat(3,157px);column-gap:3px;row-gap:27px}
.product{height:149px;border:1px solid #d9a914;background:rgba(0,0,0,.55);position:relative;color:var(--white)}
.product .thumb{height:75px;display:block;position:relative}
.product h3{margin:7px 6px 0;font-weight:600;font-size:7.5px;line-height:9px;letter-spacing:.3px;text-transform:uppercase;height:28px}
.price{position:absolute;left:6px;top:113px;font-size:8px;font-weight:600;white-space:nowrap}
.price s{color:var(--grey-light);margin-right:2px}
.stars{position:absolute;left:6px;top:124px;display:flex}
.add-cart{position:absolute;right:6px;bottom:9px;display:flex;align-items:center;gap:4px;font-size:7px;font-weight:600;text-transform:uppercase}
.quick-view{position:absolute;top:0;left:0;right:0;height:75px;background:rgba(245,193,24,.88);display:flex;flex-direction:column;align-items:center;justify-content:center;
  font-family:"Rokkitt",serif;font-size:11px;letter-spacing:1px;color:#fff;text-transform:uppercase;gap:2px;white-space:nowrap}

/* newsletter */
.newsletter{position:absolute;top:962px;left:0;width:672px;height:80px}
.newsletter h4,.follow h4{font-family:"Rokkitt",serif;font-weight:500;font-size:12px;letter-spacing:.6px;text-transform:uppercase;white-space:nowrap}
.newsletter > h4{position:absolute;left:100px;top:33px}
.email{position:absolute;left:188px;top:29px;width:122px;height:23px;border:1px solid #bbb;font-size:7.5px;color:#999;
  text-transform:uppercase;letter-spacing:.5px;padding-left:6px;display:flex;align-items:center}
.submit{position:absolute;left:312px;top:29px;width:68px;height:23px;background:var(--yellow);color:#fff;font-size:8.5px;font-weight:700;
  text-transform:uppercase;letter-spacing:.6px;display:flex;align-items:center;justify-content:center}
.follow{position:absolute;left:409px;top:31px;width:170px;display:flex;align-items:center;justify-content:space-between;white-space:nowrap}
.follow ul{display:flex;gap:4px}
.follow li{width:20px;height:20px;border-radius:50%;background:var(--yellow)}

/* footer */
.site-footer{position:absolute;top:1042px;left:0;width:672px;height:158px;background:linear-gradient(180deg,#121212,#060606);color:#8a8a8a}
.footer-col{position:absolute;top:21px}
.footer-col h5{font-family:"Rokkitt",serif;font-weight:500;font-size:11.5px;color:var(--yellow);letter-spacing:.8px;text-transform:uppercase;
  padding-bottom:3px;border-bottom:1px solid #444;width:108px;white-space:nowrap}
.col-updates h5{width:114px}
.footer-col li,.footer-col p{font-size:7.5px;line-height:10.5px;text-transform:uppercase;letter-spacing:.3px}
.footer-col li{white-space:nowrap}
.footer-col ul,.footer-col .posts{margin-top:5px}
.col-brands{left:100px}.col-cats{left:252px}.col-updates{left:427px}
.col-updates .posts{width:145px}
.legal{position:absolute;bottom:7px;width:100%;text-align:center;font-size:5.5px;letter-spacing:.4px;text-transform:uppercase;color:#777;white-space:nowrap}
</style>
</head>
<body>

<header>
  <nav class="utility">
    <a href="#">My Account</a>
    <a href="#">Gift Certificates</a>
    <a href="#">Sign in <span class="accent">or</span> Create an account</a>
    <span class="cart">My Cart (0)
      <svg width="9" height="8" viewBox="0 0 9 8"><path d="M0 1h2l1.2 4h4.3L8.5 2H2.6" fill="none" stroke="#f5c118" stroke-width="1"/><circle cx="3.6" cy="7" r=".8" fill="#f5c118"/><circle cx="7" cy="7" r=".8" fill="#f5c118"/></svg>
      <span class="dots"><i></i><i></i><i></i><i></i><i></i></span>
    </span>
  </nav>

  <div class="brand"><span class="brand-name"><i></i>Tallow Brook</span></div>
  <p class="currency">All <span>prices</span> are in <span>USD</span></p>

  <nav class="main-nav">
    <a class="active" href="#">Binoculars</a>
    <a href="#">Metal Detectors</a>
    <a href="#">Microscopes</a>
    <a href="#">Riflescopes</a>
    <a href="#">Safe</a>
    <a href="#">Shooting Accessories</a>
    <a href="#">Spotting Scopes</a>
    <a href="#">Telescopes</a>
  </nav>
</header>

<section class="hero" role="img" aria-label="Hiker sitting on a stone wall overlooking a misty mountain valley and city">
  <h1 class="hero-title">We sell all kinds of hiking equipments</h1>
  <div class="search">
    <div class="search-field">Type Product</div>
    <div class="search-btn">
      <svg width="16" height="16" viewBox="0 0 16 16"><circle cx="6.5" cy="6.5" r="5" fill="none" stroke="#fff" stroke-width="1.6"/><path d="M10.2 10.2L15 15" stroke="#fff" stroke-width="1.8"/></svg>
    </div>
  </div>
  <a class="slide-arrow prev" href="#"><svg width="6" height="10" viewBox="0 0 6 10"><path d="M5 1L1 5l4 4" fill="none" stroke="#fff"/></svg></a>
  <a class="slide-arrow next" href="#"><svg width="6" height="10" viewBox="0 0 6 10"><path d="M1 1l4 4-4 4" fill="none" stroke="#fff"/></svg></a>
  <p class="photo-credit">Dorian Pell</p>
</section>

<section class="about">
  <h2>About Us</h2>
  <p class="lead">Lorem ipsum dolor sit amet, consectetuer adipiscing</p>
  <p class="body">Lorem ipsum dolor sit amet, consectetuer adipiscing elit, sed diam nonummy nibh lorem ipsum dolor sit amet, consectetuer adipiscing elit, sed diam nonummy nibh</p>
</section>
<a class="read-more" href="#">Read More</a>

<svg width="0" height="0" style="position:absolute">
  <defs>
    <symbol id="star" viewBox="0 0 10 10"><path d="M5 .5l1.3 3 3.2.3-2.4 2.1.7 3.2L5 7.4 2.2 9.1l.7-3.2L.5 3.8l3.2-.3z"/></symbol>
    <symbol id="cart" viewBox="0 0 11 9"><path d="M0 1h2.2l1.4 5h5.3L10.5 2H3" fill="none" stroke="#f5c118" stroke-width="1.2"/><circle cx="4.2" cy="8" r=".9" fill="#f5c118"/><circle cx="8.3" cy="8" r=".9" fill="#f5c118"/></symbol>
  </defs>
</svg>

<section class="products" role="img" aria-label="Dark misty pine forest background">
  <h2>New Products</h2>
  <div class="product-grid">
    <article class="product">
      <span class="thumb" role="img" aria-label="Black solar charger with speaker on rock" style="background:linear-gradient(135deg,#6d6d6a,#2e2e2e 55%,#8b8a86)"></span>
      <h3>Portable Solar Charger Case with Speaker</h3>
      <p class="price"><s>$80.40</s> $60.78</p>
      <div class="stars"><svg width="36" height="7"><use href="#star" x="0" width="7" height="7" fill="#f5c118"/><use href="#star" x="9" width="7" height="7" fill="#fff"/><use href="#star" x="18" width="7" height="7" fill="#fff"/><use href="#star" x="27" width="7" height="7" fill="#fff"/></svg></div>
      <a class="add-cart" href="#"><svg width="11" height="9"><use href="#cart"/></svg>Cart</a>
    </article>
    <article class="product">
      <span class="thumb" role="img" aria-label="USB device charger mounted on bicycle handlebar" style="background:linear-gradient(135deg,#8a8a86,#3a3a38)"></span>
      <h3>Portable USB Device Charger with Flashlight Attachment</h3>
      <p class="price"><s>$60.75</s> $41.31</p>
      <div class="stars"><svg width="36" height="7"><use href="#star" x="0" width="7" height="7" fill="#f5c118"/><use href="#star" x="9" width="7" height="7" fill="#fff"/><use href="#star" x="18" width="7" height="7" fill="#fff"/><use href="#star" x="27" width="7" height="7" fill="#fff"/></svg></div>
      <a class="add-cart" href="#"><svg width="11" height="9"><use href="#cart"/></svg>Cart</a>
      <div class="quick-view">Quick View
        <svg width="14" height="14" viewBox="0 0 14 14"><circle cx="6" cy="6" r="4.5" fill="none" stroke="#fff" stroke-width="1.2"/><path d="M9.3 9.3L13 13M4 6h4M6 4v4" stroke="#fff" stroke-width="1.2"/></svg>
      </div>
    </article>
    <article class="product">
      <span class="thumb" role="img" aria-label="Digital heart rate monitor watch" style="background:radial-gradient(circle at 50% 45%,#9a9a9a,#e8e8e8 45%,#f6f6f6)"></span>
      <h3>Heart Rate Monitor Watch w/Calorie Counter, Traget Zone, Bicycle Mount</h3>
      <p class="price"><s>$85.75</s> $58.31</p>
      <div class="stars"><svg width="36" height="7"><use href="#star" x="0" width="7" height="7" fill="#f5c118"/><use href="#star" x="9" width="7" height="7" fill="#fff"/><use href="#star" x="18" width="7" height="7" fill="#fff"/><use href="#star" x="27" width="7" height="7" fill="#fff"/></svg></div>
      <a class="add-cart" href="#"><svg width="11" height="9"><use href="#cart"/></svg>Cart</a>
    </article>
    <article class="product">
      <span class="thumb" role="img" aria-label="Blue and white sport sunglasses" style="background:linear-gradient(135deg,#f4f4f4,#dfe4ee 50%,#f7f7f7)"></span>
      <h3>Portable Solar Charger Case with Speaker</h3>
      <p class="price"><s>$80.40</s> $60.78</p>
      <div class="stars"><svg width="36" height="7"><use href="#star" x="0" width="7" height="7" fill="#f5c118"/><use href="#star" x="9" width="7" height="7" fill="#fff"/><use href="#star" x="18" width="7" height="7" fill="#fff"/><use href="#star" x="27" width="7" height="7" fill="#fff"/></svg></div>
      <a class="add-cart" href="#"><svg width="11" height="9"><use href="#cart"/></svg>Cart</a>
    </article>
    <article class="product">
      <span class="thumb" role="img" aria-label="Grey tactical sling backpack on grass" style="background:linear-gradient(180deg,#6f7a5c,#3a3b38 50%,#7a8a55)"></span>
      <h3>Ridgepack TR-30 Tactical Sling Backpack</h3>
      <p class="price"><s>$80.40</s> $60.78</p>
      <div class="stars"><svg width="36" height="7"><use href="#star" x="0" width="7" height="7" fill="#f5c118"/><use href="#star" x="9" width="7" height="7" fill="#fff"/><use href="#star" x="18" width="7" height="7" fill="#fff"/><use href="#star" x="27" width="7" height="7" fill="#fff"/></svg></div>
      <a class="add-cart" href="#"><svg width="11" height="9"><use href="#cart"/></svg>Cart</a>
    </article>
    <article class="product">
      <span class="thumb" role="img" aria-label="Black tactical backpack with gear" style="background:linear-gradient(135deg,#2a2520,#151311 50%,#5a4a35)"></span>
      <h3>Ridgepack TR-20 Tactical Backpack</h3>
      <p class="price"><s>$80.40</s> $60.78</p>
      <div class="stars"><svg width="36" height="7"><use href="#star" x="0" width="7" height="7" fill="#f5c118"/><use href="#star" x="9" width="7" height="7" fill="#fff"/><use href="#star" x="18" width="7" height="7" fill="#fff"/><use href="#star" x="27" width="7" height="7" fill="#fff"/></svg></div>
      <a class="add-cart" href="#"><svg width="11" height="9"><use href="#cart"/></svg>Cart</a>
    </article>
  </div>
</section>

<section class="newsletter">
  <h4>Newsletter</h4>
  <div class="email">Email</div>
  <a class="submit" href="#">Submit</a>
  <div class="follow">
    <h4>Follow Us</h4>
    <ul><li></li><li></li><li></li><li></li></ul>
  </div>
</section>

<footer class="site-footer">
  <div class="footer-col col-brands">
    <h5>Brands</h5>
    <ul><li>Vantrel</li><li>View all brands</li></ul>
  </div>
  <div class="footer-col col-cats">
    <h5>Categories</h5>
    <ul><li>Binoculars</li><li>Metal Detectors</li><li>Microscopes</li><li>Riflescopes</li><li>Safe</li><li>Telescopes</li><li>View all categories</li></ul>
  </div>
  <div class="footer-col col-updates">
    <h5>Recent Updates</h5>
    <div class="posts"><p>Your first blog post!</p><p>Welcome to your blog! A blog is a great place to share details on your ...</p></div>
  </div>
  <p class="legal">All prices are in USD. © 2015 Tallow Brook. Sitemap | Shopping Cart Software by Shelvora</p>
</footer>

</body>
</html>
```